IT company needs A4 Cover page design for our sales proposals

We need a A4 cover page designed for use with our Tallyforge Offer (Brivex) quoting software. This cover page will be used for PDF and print.

We are a Managed IT Service Provider serving small to medium sized businesses based in the UK.

The design needs to convey professionalism, technology and people

Must incorporate the new Banner Ad theme we have just had designed through this website (Pixelmarq project number 5829463 https://www.pixelmarq.co.uk/project-progress/overview.aspx?briefId=5829463)

It is recommended to be 1240 x 1754

Target Market(s)

Small to medium sized companies - verticals include Healthcare, Accounting, Engineering, Manufacturing

Industry/Entity Type

It Company

Colors
f37122
000000
b7b7b7
eaeaea

Requirements
Must have
• Must incorporate our logo, strap line and picture of the person as per Pixelmarq project 5829463 https://www.pixelmarq.co.uk/project-progress/overview.aspx?briefId=5829463
• Must convey business, professionalism, technology and people
• Must have a picture of a person using technlogy
• Use our corporate colours of orange, black, grey & white as per www.lumoravex.co.uk

```html
<!DOCTYPE html>
<html lang="en">
<head>
<meta charset="utf-8">
<title>Lumoravex Proposal Cover</title>
<link rel="stylesheet" href="https://fonts.googleapis.com/css2?family=Exo+2:wght@400;600&family=Raleway:wght@400;500;700&display=swap">
<style>
  :root {
    --orange: #f37122;
    --black: #000000;
    --grey: #b7b7b7;
    --light: #eaeaea;
    --white: #ffffff;
    --ink: #222222;
    --backdrop: #d9d4cc;
  }
  * { box-sizing: border-box; margin: 0; padding: 0; }
  html, body { width: 1189px; height: 1200px; overflow: hidden; background: var(--backdrop); }
  .cover {
    position: absolute; left: 177px; top: 10px;
    width: 835px; height: 1181px;
    background: var(--white);
    font-family: "Raleway", sans-serif;
    box-shadow: 0 2px 10px rgba(0,0,0,.18);
    overflow: hidden;
  }
  .header { position: absolute; left: 0; top: 0; width: 835px; height: 125px; background: var(--light); }
  .header svg { position: absolute; left: 0; top: 0; }
  .header-photo {
    position: absolute; left: 590px; top: 0; width: 245px; height: 125px;
    clip-path: polygon(88px 0, 245px 0, 245px 125px, 0 125px);
    background:
      radial-gradient(ellipse 40px 55px at 105px 75px, #c9d0dc 0%, rgba(201,208,220,0) 100%),
      radial-gradient(ellipse 45px 28px at 170px 95px, #8e8e8e 0%, rgba(142,142,142,0) 100%),
      radial-gradient(ellipse 18px 22px at 110px 25px, #6b5a4e 0%, rgba(107,90,78,0) 100%),
      linear-gradient(90deg, #eef0f2 0%, #f7f7f7 60%, #dcdcdc 100%);
  }
  .brand {
    position: absolute; left: 48px; top: 46px;
    display: flex; align-items: center; gap: 10px;
  }
  .brand-dot { width: 14px; height: 14px; border-radius: 50%; background: var(--orange); }
  .brand-name { font-weight: 700; font-size: 32px; letter-spacing: 1px; color: var(--black); }
  .strapline {
    position: absolute; left: 395px; top: 36px; width: 230px;
    font-family: "Exo 2", sans-serif; font-size: 13px; line-height: 17px;
    color: var(--white); text-align: center; letter-spacing: .6px; text-transform: uppercase;
  }
  .rule-black { position: absolute; left: 0; top: 131px; width: 835px; height: 4px; background: var(--black); }
  .rule-fade { position: absolute; left: 0; top: 141px; width: 835px; height: 8px;
    background: linear-gradient(90deg, var(--orange) 0%, #fbd2b6 45%, #fde6d6 60%, var(--orange) 100%); }
  .rule-orange { position: absolute; left: 0; height: 8px; width: 835px; background: var(--orange); }
  .hero-photo {
    position: absolute; left: 0; top: 237px; width: 835px; height: 512px;
    background:
      radial-gradient(ellipse 160px 190px at 300px 180px, #5c5c5c 0%, rgba(92,92,92,0) 100%),
      radial-gradient(ellipse 170px 200px at 470px 150px, #6e6e6e 0%, rgba(110,110,110,0) 100%),
      radial-gradient(ellipse 190px 120px at 420px 390px, #8a8a8a 0%, rgba(138,138,138,0) 100%),
      radial-gradient(ellipse 170px 110px at 150px 420px, #9c9c9c 0%, rgba(156,156,156,0) 100%),
      linear-gradient(90deg, #bdbdbd 0%, #d6d6d6 20%, #cfcfcf 55%, #e8e8e8 75%, #f6f6f6 100%);
  }
  .city-photo {
    position: absolute; left: 0; top: 772px; width: 835px; height: 363px;
    background:
      radial-gradient(ellipse 120px 160px at 120px 250px, #cfcfcf 0%, rgba(207,207,207,0) 100%),
      radial-gradient(ellipse 140px 190px at 420px 230px, #d3d3d3 0%, rgba(211,211,211,0) 100%),
      radial-gradient(ellipse 160px 200px at 690px 220px, #cdcdcd 0%, rgba(205,205,205,0) 100%),
      linear-gradient(180deg, #fcfcfc 0%, #f0f0f0 30%, #e2e2e2 60%, #e8e8e8 100%);
  }
  .proposal-banner { position: absolute; left: 0; top: 845px; }
  .proposal-title {
    position: absolute; left: 49px; top: 859px;
    font-weight: 700; font-size: 23px; color: var(--white); letter-spacing: .3px;
  }
  .details { position: absolute; top: 1044px; }
  .details h2 {
    font-weight: 500; font-size: 20px; color: var(--black);
    padding-bottom: 2px; border-bottom: 1.5px solid var(--ink); display: inline-block; min-width: 187px;
  }
  .details p { font-size: 13px; line-height: 17px; color: #333; margin-top: 4px; }
  .details p + p { margin-top: 0; }
  .details.proposal { left: 45px; }
  .details.client { left: 333px; }
  .details.client h2 { min-width: 157px; }
  .footer-rule { position: absolute; left: 0; top: 1140px; width: 835px; height: 3px; background: var(--black); }
  .footer {
    position: absolute; left: 0; top: 1146px; width: 835px; height: 35px;
    background: linear-gradient(90deg, var(--orange) 0%, #f9c9a6 30%, #fbd8bf 50%, #f9c9a6 70%, var(--orange) 100%);
    display: flex; align-items: center; justify-content: center; gap: 48px;
    font-size: 14px; color: var(--ink);
  }
  .contact { display: flex; align-items: center; gap: 6px; }
  .divider { width: 1.5px; height: 16px; background: var(--ink); }
</style>
</head>
<body>
<main class="cover">
  <header class="header">
    <svg width="835" height="125" viewBox="0 0 835 125">
      <polygon points="414,18 428,18 343,108 329,108" fill="var(--black)"/>
      <polygon points="429,0 674,0 574,125 329,125" fill="var(--orange)"/>
      <polygon points="668,18 682,18 603,110 589,110" fill="var(--black)"/>
    </svg>
    <div class="header-photo" role="img" aria-label="Photo of a man in a shirt working at a laptop in an office"></div>
    <div class="brand">
      <span class="brand-name">LUMORAVEX</span>
      <span class="brand-dot"></span>
    </div>
    <p class="strapline">Bringing enterprise- level<br>solutions to East Anglia<br>small businesses</p>
  </header>

  <div class="rule-black"></div>
  <div class="rule-fade"></div>
  <div class="rule-orange" style="top:222px"></div>

  <div class="hero-photo" role="img" aria-label="Black and white photo of a smiling couple looking at a smartphone beside a laptop"></div>

  <div class="rule-orange" style="top:762px"></div>

  <div class="city-photo" role="img" aria-label="Faded grey photo of a city skyline"></div>

  <svg class="proposal-banner" width="660" height="56" viewBox="0 0 660 56">
    <polygon points="0,0 650,0 606,56 0,56" fill="var(--orange)"/>
  </svg>
  <h1 class="proposal-title">WE HAVE PREPARED A PROPOSAL FOR YOU</h1>

  <section class="details proposal">
    <h2>Standard MSP CSP</h2>
    <p>Proposal # DJ-000307</p>
    <p>Version 1</p>
  </section>
  <section class="details client">
    <h2>Hollowmere</h2>
    <p>Elena Marsh</p>
    <p>Elena.Marsh@mailbox.com</p>
  </section>

  <div class="footer-rule"></div>
  <footer class="footer">
    <span class="contact">
      <svg width="16" height="14" viewBox="0 0 16 14"><path d="M1 4 Q8 -1 15 4 L13 6 L11 4.5 L5 4.5 L3 6 Z M3 7 L13 7 L14 13 L2 13 Z" fill="var(--ink)"/></svg>
      (01) 4872 3310
    </span>
    <span class="divider"></span>
    <span class="contact">
      <svg width="14" height="10" viewBox="0 0 14 10"><rect x="0.5" y="0.5" width="13" height="9" fill="var(--ink)"/><path d="M0.5 0.5 L7 5.5 L13.5 0.5" stroke="#fbd8bf" fill="none"/></svg>
      Info@lumoravex.co.uk
    </span>
    <span class="divider"></span>
    <span class="contact">
      <svg width="14" height="14" viewBox="0 0 14 14"><circle cx="7" cy="7" r="6" fill="none" stroke="var(--ink)" stroke-width="1.3"/><ellipse cx="7" cy="7" rx="2.6" ry="6" fill="none" stroke="var(--ink)" stroke-width="1"/><line x1="1" y1="7" x2="13" y2="7" stroke="var(--ink)"/></svg>
      www.lumoravex.co.uk
    </span>
  </footer>
</main>
</body>
</html>
```